Business Cards that are elegant and wow

I want to create and print business cards that represent my brand and stand out from the rest. We want to ensure they stay in our branding and the integrity is not lost. I am happy to look at different shapes like square etc.

It will be printed on very thick cards and will be stylish .

I want to create and print business cards that represent my brand and stand out from the rest. We want to ensure they stay in ur branding and the integrity is not lost. I am happy to look at different shapes like square etc.

Target Market(s)

real estate professionals

Industry/Entity Type

Real Estate

Contact Information for Business Card

Maren Holt
hello@brightfernrealty.com.au
brightfernrealty.com.au
0487 316 252 (SMS)

Colors

Designer to choose colors to be used in the design.

Requirements
Must have
• My logo
• email
• website
• Name
Nice to have
• I like the idea of printing with foil or spot gloss. You want it to stand out in a sea.
Should not have
• I would like you to stay in my colour themes. Don't change the colour of my logo

```html
<!DOCTYPE html>
<html lang="en">
<head>
<meta charset="utf-8">
<title>Bright Fern Realty — Business Card</title>
<link href="https://fonts.googleapis.com/css2?family=Source+Sans+3:wght@400;600;700&display=swap" rel="stylesheet">
<style>
  :root {
    --sky: #00adee;
    --ink: #070707;
    --magenta: #ec1277;
    --paper: #ffffff;
    --stage: #fdfdfd;
  }
  * { margin: 0; padding: 0; box-sizing: border-box; }
  html, body { width: 1200px; height: 900px; overflow: hidden; background: var(--stage); }
  body { position: relative; font-family: "Source Sans 3", "Myriad Pro", sans-serif; }

  .card {
    position: absolute;
    width: 566px;
    height: 338px;
    background: var(--paper);
    border-radius: 22px;
    overflow: hidden;
    box-shadow: 0 14px 30px rgba(0,0,0,0.35), 0 2px 8px rgba(0,0,0,0.2);
  }
  .card--front { left: 319px; top: 72px; }
  .card--back  { left: 317px; top: 485px; }

  .band { position: absolute; left: 0; width: 100%; }
  .band--sky { background: var(--sky); }
  .band--ink { background: var(--ink); }

  /* front */
  .card--front .band--top    { top: 38px;  height: 79px; }
  .card--front .band--middle { top: 117px; height: 109px; }
  .card--front .band--bottom { top: 226px; height: 78px; }

  .brand {
    position: absolute;
    left: 23px; top: 25px;
    display: flex; align-items: center; gap: 12px;
  }
  .brand__dot {
    width: 58px; height: 58px;
    border: 3px solid var(--magenta);
    border-radius: 50%;
  }
  .brand__name {
    color: var(--sky);
    font-weight: 600;
    font-size: 27px;
    letter-spacing: 0.5px;
    text-transform: uppercase;
    line-height: 1;
  }

  .holder {
    position: absolute;
    right: 27px; top: 36px;
    text-align: right;
  }
  .holder__name {
    color: var(--sky);
    font-weight: 700;
    font-size: 26px;
    letter-spacing: 1.5px;
    text-transform: uppercase;
    line-height: 1;
  }
  .holder__role {
    margin-top: 6px;
    color: var(--magenta);
    font-size: 14px;
    line-height: 1;
  }

  /* back */
  .card--back .band--top    { top: 37px;  height: 78px; }
  .card--back .band--middle { top: 115px; height: 109px; }
  .card--back .band--bottom { top: 224px; height: 78px; }

  .accent { position: absolute; height: 10px; background: var(--magenta); }
  .accent--left   { left: 0;     top: 37px;  width: 238px; }
  .accent--right  { left: 324px; top: 37px;  width: 240px; }
  .accent--bottom { left: 162px; top: 292px; width: 240px; }

  .contact {
    position: absolute;
    color: var(--paper);
    font-size: 15px;
    line-height: 1;
  }
  .contact--phone { left: 57px; top: 67px; }
  .contact--email { right: 28px; top: 67px; }
  .contact--web   { left: 0; width: 100%; text-align: center; top: 234px; }

  .icon {
    position: absolute;
    top: 134px;
    width: 70px; height: 70px;
  }
  .icon--phone { left: 84px; }
  .icon--web   { left: 247px; }
  .icon--mail  { left: 409px; }
</style>
</head>
<body>

<section class="card card--front">
  <div class="band band--sky band--top"></div>
  <div class="band band--ink band--middle">
    <div class="brand">
      <span class="brand__dot"></span>
      <span class="brand__name">Bright Fern Realty</span>
    </div>
    <div class="holder">
      <div class="holder__name">Maren Holt</div>
      <div class="holder__role">Owner</div>
    </div>
  </div>
  <div class="band band--sky band--bottom"></div>
</section>

<section class="card card--back">
  <div class="band band--sky band--top"></div>
  <div class="accent accent--left"></div>
  <div class="accent accent--right"></div>
  <p class="contact contact--phone">0487 316 252 (SMS)</p>
  <p class="contact contact--email">hello@brightfernrealty.com.au</p>

  <div class="band band--ink band--middle"></div>

  <svg class="icon icon--phone" viewBox="0 0 70 70" aria-label="Phone">
    <circle cx="35" cy="35" r="33" fill="none" stroke="var(--sky)" stroke-width="3"/>
    <path d="M26 22 l5 -2 l4 8 l-3 3 q3 6 9 9 l3 -3 l8 4 l-2 5 q-3 3 -8 1 q-12 -6 -18 -18 q-2 -5 2 -7z" fill="var(--magenta)"/>
  </svg>

  <svg class="icon icon--web" viewBox="0 0 70 70" aria-label="Website">
    <circle cx="35" cy="35" r="33" fill="none" stroke="var(--sky)" stroke-width="3"/>
    <circle cx="35" cy="35" r="17" fill="var(--magenta)"/>
    <path d="M18 35 h34 M35 18 v34 M35 18 q-10 17 0 34 M35 18 q10 17 0 34" fill="none" stroke="var(--ink)" stroke-width="1.6"/>
  </svg>

  <svg class="icon icon--mail" viewBox="0 0 70 70" aria-label="Email">
    <circle cx="35" cy="35" r="33" fill="none" stroke="var(--sky)" stroke-width="3"/>
    <rect x="21" y="25" width="28" height="20" fill="var(--magenta)"/>
    <path d="M21 25 l14 11 l14 -11 M21 45 l11 -10 M49 45 l-11 -10" fill="none" stroke="var(--ink)" stroke-width="1.6"/>
  </svg>

  <div class="band band--sky band--bottom"></div>
  <p class="contact contact--web">brightfernrealty.com.au</p>
  <div class="accent accent--bottom"></div>
</section>

</body>
</html>
```